1920s Holiday Casino Night Invite (work event)

Looking for a 1920's theme invite for our holiday party that will include casino games. Would love to have an invite that includes the Holiday, Casino and 1920s theme with still the traditional Christmas feeling.

Event Date: Saturday, December 16th from 6-9pm
Address: Calloway Co.
28730 n. 47th lane, Arvada, CO

1920s costume contest
Prizes, Food, Drink and Apps included

Target Market(s)

Men

Industry/Entity Type

Construction Company

Font styles to use
Serif
Sans Serif
Decorative
Script

Colors

Designer to choose colors to be used in the design.

Requirements
Must have
• Most have Holiday and 1920s theme
Nice to have
• Most have Holiday theme and pay into the fact its a 1920s casino night
Should not have
• Should not have nontraditional (holiday) colors

```html
<!DOCTYPE html>
<html lang="en">
<head>
<meta charset="utf-8">
<title>Holiday Party Invitation</title>
<link rel="stylesheet" href="https://fonts.googleapis.com/css2?family=Poiret+One&family=Noto+Serif&display=swap">
<style>
  :root {
    --page: #ffffff;
    --card: #000000;
    --gold: #e9d38c;
    --gold-light: #f3e3a6;
    --gold-deep: #b98a4e;
    --bronze: #8a5a2b;
    --silver: #6d6d6d;
    --silver-dark: #3a3a3a;
  }
  * { margin: 0; padding: 0; box-sizing: border-box; }
  html, body { width: 900px; height: 1200px; overflow: hidden; background: var(--page); }
  .canvas { position: relative; width: 900px; height: 1200px; }
  .invite-card {
    position: absolute; left: 47px; top: 34px; width: 806px; height: 1129px;
    background: var(--card);
  }
  .frame-outer {
    position: absolute; left: 32px; top: 29px; width: 742px; height: 1069px;
    border: 12px solid transparent;
    border-image: linear-gradient(135deg, var(--gold-light), var(--gold-deep) 35%, var(--gold) 60%, var(--bronze)) 1;
  }
  .frame-inner {
    position: absolute; left: 50px; top: 47px; width: 706px; height: 1033px;
    border: 2px solid var(--gold-deep);
  }
  .corner-ornament {
    position: absolute; width: 92px; height: 92px;
    background: linear-gradient(135deg, var(--gold-light), var(--gold) 45%, var(--gold-deep));
  }
  .corner-ornament.tl { left: 32px; top: 29px; }
  .corner-ornament.tr { right: 32px; top: 29px; }
  .corner-ornament.bl { left: 32px; bottom: 29px; }
  .corner-ornament.br { right: 32px; bottom: 29px; }
  .dice-art {
    position: absolute; left: 355px; top: 100px; width: 100px; height: 70px;
    border-radius: 12px;
    background: radial-gradient(ellipse at 50% 50%, #8a8a8a, #4a4a4a 60%, rgba(0,0,0,0) 100%);
  }
  .title-rule {
    position: absolute; left: 73px; width: 660px; height: 2px; background: var(--gold);
  }
  .title-rule.top { top: 217px; }
  .title-rule.bottom { top: 321px; }
  .event-title {
    position: absolute; left: 0; top: 216px; width: 806px; text-align: center;
    font-family: "Poiret One", sans-serif; font-size: 94px; line-height: 104px;
    color: var(--gold); letter-spacing: 3px; white-space: nowrap;
  }
  .event-details {
    position: absolute; left: 0; top: 342px; width: 806px; text-align: center;
    font-family: "Noto Serif", serif; font-size: 31px; line-height: 38px; color: var(--gold);
  }
  .star-divider { position: absolute; left: 111px; top: 503px; width: 615px; height: 36px; }
  .tree-art {
    position: absolute; left: 219px; top: 561px; width: 361px; height: 476px;
    background: radial-gradient(ellipse 50% 55% at 50% 60%, #4e4e4e, #333333 55%, rgba(0,0,0,0) 100%);
  }
  .side-note {
    position: absolute; width: 240px; text-align: center;
    font-family: "Noto Serif", serif; font-size: 24px; line-height: 32px; color: var(--gold);
  }
  .side-note.costume { left: 57px; top: 816px; }
  .side-note.perks { left: 517px; top: 812px; }
</style>
</head>
<body>
<div class="canvas">
  <section class="invite-card">
    <div class="frame-outer"></div>
    <div class="frame-inner"></div>
    <div class="corner-ornament tl" role="img" aria-label="Art deco gold key corner ornament"></div>
    <div class="corner-ornament tr" role="img" aria-label="Art deco gold key corner ornament"></div>
    <div class="corner-ornament bl" role="img" aria-label="Art deco gold key corner ornament"></div>
    <div class="corner-ornament br" role="img" aria-label="Art deco gold key corner ornament"></div>

    <div class="dice-art" role="img" aria-label="Pair of grey casino dice"></div>

    <div class="title-rule top"></div>
    <h1 class="event-title">HOLIDAY PARTY</h1>
    <div class="title-rule bottom"></div>

    <p class="event-details">
      Event Date: Saturday, December 16th<br>
      from 6-9pm<br>
      Address: Calloway Co.<br>
      28730 n. 47th lane, Arvada, CO
    </p>

    <svg class="star-divider" viewBox="0 0 615 36" aria-hidden="true">
      <defs>
        <linearGradient id="rule-left" x1="0" x2="1"><stop offset="0" stop-color="#e9d38c" stop-opacity="0"/><stop offset="1" stop-color="#e9d38c"/></linearGradient>
        <linearGradient id="rule-right" x1="0" x2="1"><stop offset="0" stop-color="#e9d38c"/><stop offset="1" stop-color="#e9d38c" stop-opacity="0"/></linearGradient>
      </defs>
      <rect x="0" y="17" width="265" height="2" fill="url(#rule-left)"/>
      <rect x="350" y="17" width="265" height="2" fill="url(#rule-right)"/>
      <polygon fill="#e9d38c" points="307.5,1 312,13 325,13 314.5,21 318.5,34 307.5,26 296.5,34 300.5,21 290,13 303,13"/>
    </svg>

    <div class="tree-art" role="img" aria-label="Swirling silver filigree Christmas tree"></div>

    <p class="side-note costume">1920s Costume<br>Contest</p>
    <p class="side-note perks">Prizes, Food,<br>Drink and<br>Apps included</p>
  </section>
</div>
</body>
</html>
```